Covid-19 Mortgage Housing Market Coaching

I need a one page 8.5 x 11 printable infographic to describe the following:
Housing and Mortgage Market Coach
Through your Employer Home-ownership Benefit
The Coronavirus has resulted in an unprecedented Government coordination to reduce the spread of the virus, as such, has altered the way we live and work.
As each of us looks to the potential impact of the Coronavirus to our financial stability, it can be difficult to obtain trusted information to help make sound financial decisions.
As part of your employee home ownership program through your employer, you have access to this educational coaching on the below topics:
• What is happening in the stock market and why it is happening.
• Motivation behind Feds cutting rates and how that translates to the lending market.
• Discuss the future of interest rates.
• Discuss the future of the housing market. How will the spring and summer housing markets be effected?
• Everyone says to refinance now. Is that really in my best interest? Learn how to do a refinance analysis and determine if refinancing is right for you.
Having a better understanding of what is happening in the financial markets, with interest rates and the housing market can help you successfully navigate this rapidly evolving situation.
Please be sure that our phone number is prominently displayed 1-800-529-8172 and our web address www.brightkeylending.example

```html
<!DOCTYPE html>
<html lang="en">
<head>
<meta charset="utf-8">
<title>Housing and Mortgage Market Coach</title>
<link rel="stylesheet" href="https://fonts.googleapis.com/css2?family=Source+Sans+3:wght@400;600;700&display=swap">
<style>
  :root {
    --teal: #0b7b89;
    --teal-dark: #0a6470;
    --charcoal: #3a3d3e;
    --lime: #b2d457;
    --lime-text: #b7d85c;
    --ink: #1f2326;
    --white: #ffffff;
    --footer-text: #5f7277;
  }
  * { margin: 0; padding: 0; box-sizing: border-box; }
  html, body { width: 927px; height: 1200px; overflow: hidden; background: var(--white); }
  body { font-family: "Source Sans 3", "Myriad Pro", sans-serif; color: var(--ink); }
  .page { position: relative; width: 927px; height: 1200px; border: 2px solid var(--teal); overflow: hidden; }

  .header { position: absolute; left: 0; top: 0; width: 100%; height: 210px; background: var(--teal); overflow: hidden; }
  .header-band { position: absolute; left: 0; top: 210px; width: 100%; height: 16px; background: var(--charcoal); }
  .header-glow { position: absolute; left: 300px; top: 208px; width: 420px; height: 3px;
    background: linear-gradient(90deg, transparent, #cfe59a, transparent); }
  .header-title { position: absolute; left: 42px; top: 40px; color: var(--white); font-weight: 700;
    font-size: 46px; line-height: 56px; letter-spacing: 0.5px; }
  .header-art { position: absolute; left: 0; top: 0; }

  .main-heading { position: absolute; right: 34px; top: 250px; text-align: right; color: var(--teal);
    font-weight: 700; font-size: 47px; line-height: 56px; letter-spacing: 0.3px; }

  .slant-panel { position: absolute; }
  .slant-panel p { position: absolute; font-size: 15.5px; line-height: 20px; }
  .intro-panel { left: 0; top: 378px; width: 520px; height: 130px; }
  .intro-panel p { left: 38px; top: 17px; width: 450px; }
  .impact-panel { left: 460px; top: 469px; width: 467px; height: 130px; }
  .impact-panel p { right: 34px; top: 25px; width: 380px; text-align: right; }

  .topics-tab { position: absolute; left: 144px; top: 643px; width: 638px; height: 54px;
    background: var(--teal); border-radius: 8px 8px 0 0; color: var(--white); font-weight: 700;
    font-size: 16px; line-height: 21px; text-align: center; padding-top: 6px; }
  .topics-box { position: absolute; left: 44px; top: 695px; width: 837px; height: 164px;
    background: var(--charcoal); border-radius: 10px; padding: 12px 26px 0 27px; }
  .topics-list { list-style: none; color: var(--lime-text); font-size: 16.3px; line-height: 22px; }
  .topics-list li::before { content: "• "; }

  .closing-box { position: absolute; left: 129px; top: 897px; width: 668px; height: 100px;
    background: var(--lime); border-radius: 10px; text-align: center; font-size: 16.5px;
    line-height: 22px; padding-top: 16px; }

  .brand { position: absolute; left: 280px; top: 1040px; width: 400px; }
  .brand-name { display: flex; align-items: center; gap: 12px; color: #1d3f6e; font-weight: 700;
    font-size: 30px; line-height: 36px; }
  .brand-mark { width: 22px; height: 22px; background: var(--lime); }
  .brand-tagline { margin-left: 124px; margin-top: 4px; font-size: 15px; color: #44484a; }

  .footer { position: absolute; left: 0; bottom: 0; width: 100%; height: 52px; background: var(--teal); }
  .contact { position: absolute; top: 13px; display: flex; align-items: center; gap: 4px;
    color: var(--footer-text); font-size: 17px; }
  .contact-phone { left: 306px; }
  .contact-web { left: 478px; }
  .contact-divider { position: absolute; left: 461px; top: 9px; width: 2px; height: 32px; background: var(--white); }
</style>
</head>
<body>
<div class="page">

  <header class="header">
    <svg class="header-art" width="927" height="210" viewBox="0 0 927 210">
      <defs>
        <radialGradient id="particle" cx="50%" cy="50%" r="50%">
          <stop offset="0%" stop-color="#7cc242"/>
          <stop offset="70%" stop-color="#3fa843"/>
          <stop offset="100%" stop-color="#3fa843" stop-opacity="0"/>
        </radialGradient>
      </defs>
      <g class="growth-chart" fill="#09616d">
        <rect x="564" y="185" width="34" height="25"/>
        <rect x="621" y="138" width="32" height="72"/>
        <rect x="678" y="165" width="32" height="45"/>
        <rect x="734" y="144" width="32" height="66"/>
        <rect x="790" y="90" width="32" height="120"/>
        <rect x="846" y="55" width="32" height="155"/>
      </g>
      <polyline points="560,200 640,150 700,170 750,150 810,110 870,60 927,42"
        fill="none" stroke="#2f97a4" stroke-width="1.5"/>
      <g role="img" aria-label="Coronavirus particle illustrations">
        <circle cx="515" cy="95" r="42" fill="url(#particle)"/>
        <circle cx="706" cy="53" r="27" fill="url(#particle)"/>
        <circle cx="829" cy="125" r="62" fill="url(#particle)"/>
        <circle cx="379" cy="178" r="22" fill="url(#particle)"/>
        <circle cx="657" cy="192" r="14" fill="url(#particle)"/>
      </g>
    </svg>
    <h1 class="header-title">CORONAVIRUS<br>(COVID-19)</h1>
  </header>
  <div class="header-band"></div>
  <div class="header-glow"></div>

  <h2 class="main-heading">HOUSING AND MORTGAGE<br>MARKET COACH</h2>

  <section class="slant-panel intro-panel">
    <svg width="520" height="130" viewBox="0 0 520 130">
      <polygon points="20,0 520,0 470,124 20,124" fill="var(--lime)"/>
      <polyline points="470,124 520,0" stroke="#2f3436" stroke-width="2" fill="none"/>
      <rect x="0" y="0" width="20" height="128" fill="var(--teal)"/>
    </svg>
    <p>Through your Employer Home-ownership Benefit<br>The Coronavirus has resulted in an unprecedented Government coordination to reduce the spread of the virus, as such, has altered the way we live and work.</p>
  </section>

  <section class="slant-panel impact-panel">
    <svg width="467" height="130" viewBox="0 0 467 130">
      <polygon points="55,0 445,0 445,127 3,127" fill="var(--lime)"/>
      <line x1="3" y1="128" x2="40" y2="30" stroke="#2f3436" stroke-width="2"/>
      <rect x="445" y="0" width="22" height="127" fill="var(--teal)"/>
    </svg>
    <p>As each of us looks to the potential impact of the Coronavirus to our financial stability, it can be difficult to obtain trusted information to help make sound financial decisions.</p>
  </section>

  <div class="topics-tab">As part of your employee home ownership program through your employer,<br>you have access to this educational coaching on the below topics:</div>
  <section class="topics-box">
    <ul class="topics-list">
      <li>What is happening in the stock market and why it is happening.</li>
      <li>Motivation behind Feds cutting rates and how that translates to the lending market.</li>
      <li>Discuss the future of interest rates.</li>
      <li>Discuss the future of the housing market. How will the spring and summer housing markets be effected ?</li>
      <li>Everyone says to refinance now. Is that really in my best interest? Learn how to do a refinance analysis and determine if refinancing is right for you.</li>
    </ul>
  </section>

  <section class="closing-box">
    <p>Having a better understanding of what is happening in the financial markets,<br>with interest rates and the housing market can help you successfully navigate this<br>rapidly evolving situation.</p>
  </section>

  <div class="brand">
    <div class="brand-name"><span class="brand-mark"></span>Brightkey Lending</div>
    <div class="brand-tagline">Employee Home Ownership Program</div>
  </div>

  <footer class="footer">
    <div class="contact contact-phone">
      <svg width="20" height="26" viewBox="0 0 20 26" aria-hidden="true">
        <path d="M5 2 L9 2 L10 8 L7 10 C8 14 10 17 13 19 L16 17 L19 21 L17 25 C9 24 2 15 2 6 Z" fill="#3d4447"/>
      </svg>
      <span>1-800-529-8172</span>
    </div>
    <div class="contact-divider"></div>
    <div class="contact contact-web">
      <svg width="30" height="30" viewBox="0 0 30 30" aria-hidden="true" fill="none" stroke="#3d4447" stroke-width="2">
        <circle cx="15" cy="15" r="13"/>
        <ellipse cx="15" cy="15" rx="6" ry="13"/>
        <line x1="2" y1="15" x2="28" y2="15"/>
        <line x1="4" y1="8" x2="26" y2="8"/>
        <line x1="4" y1="22" x2="26" y2="22"/>
      </svg>
      <span>www.brightkeylending.example</span>
    </div>
  </footer>
</div>
</body>
</html>
```